Corporate Intelligence Agency seeks redesign *

Varnholt Insight is a business intelligence firm made up of former special operations and intelligence professionals. Our vibe is quiet professionals that get the job done by whatever means necessary.
Our aesthetic is clean, sleek, and monochromatic. We prefer the texture contrasts over colors. Slick white or black, playing up textures, and bold block lettering, and simplicity are what we are looking for in a design.

The logo would preferably pay homage to our military/special operations roots, and the culture of changing for the better (alchemy) that we embody all while remaining simple.

Target Market(s)

C-Level executives with a taste for the simple over the extravagant, and cut right to the chase

Industry/Entity Type

Management Solution

Contact Information for Business Card

Back is matte black with a glossy black logo to contrast. The front has the logo, with space on the bottom left for name and contact

Logo Text

Varnholt Ins.

Logo styles of interest
Abstract Logo
Wordmark Logo
Lettermark Logo
Font styles to use
Serif
Sans Serif
Script

Requirements
Must have
• Monochromatic, play on texture within card (the card ought to be memorable to hold), solid/clean lettering. Logo should be simple and sleek.
Nice to have
• If the logo can tie alchemy and intelligence/spy genre. 3d textures
Should not have
• Nothing overtly military. No colors outside of the monochromatic spectrum

```html
<!DOCTYPE html>
<html lang="en">
<head>
<meta charset="utf-8">
<title>Varnholt Insight — Business Cards</title>
<link href="https://fonts.googleapis.com/css2?family=Montserrat:wght@300;400&family=Oswald:wght@300&display=swap" rel="stylesheet">
<style>
  :root {
    --page: #ffffff;
    --ink-black: #000000;
    --ink-graphite: #2c2c2e;
    --type-white: #ffffff;
    --type-muted: #7a7a7c;
    --type-faint: #5c5c5e;
  }
  html, body {
    margin: 0;
    padding: 0;
    width: 1200px;
    height: 1000px;
    overflow: hidden;
    background: var(--page);
  }
  .canvas {
    position: relative;
    width: 1200px;
    height: 1000px;
  }
  .card {
    position: absolute;
    width: 550px;
    height: 315px;
    overflow: hidden;
  }
  .card svg.facets {
    position: absolute;
    inset: 0;
    width: 100%;
    height: 100%;
  }
  .card--front { left: 317px; top: 134px; }
  .card--back  { left: 321px; top: 514px; }

  .wordmark {
    position: absolute;
    left: 0;
    right: 0;
    top: 138px;
    text-align: center;
    font-family: "Montserrat", sans-serif;
    font-weight: 300;
    font-size: 27px;
    letter-spacing: 0.22em;
    color: var(--type-white);
    white-space: nowrap;
  }

  .holder {
    position: absolute;
    left: 0;
    right: 0;
    text-align: center;
    font-family: "Montserrat", sans-serif;
    color: var(--type-muted);
  }
  .holder__name {
    top: 36px;
    font-size: 21px;
    font-weight: 400;
    letter-spacing: 0.2em;
  }
  .holder__title {
    top: 66px;
    font-size: 12px;
    font-weight: 400;
    letter-spacing: 0.45em;
  }
  .holder__contact {
    top: 252px;
    font-family: "Oswald", sans-serif;
    font-weight: 300;
    font-size: 14px;
    letter-spacing: 0.45em;
    color: var(--type-faint);
  }
</style>
</head>
<body>
<main class="canvas">

  <section class="card card--front" aria-label="Card front">
    <svg class="facets" viewBox="0 0 550 315" preserveAspectRatio="none" aria-hidden="true">
      <rect width="550" height="315" fill="var(--ink-black)"/>
      <polygon points="0,0 275,157.5 0,315" fill="var(--ink-graphite)"/>
      <polygon points="550,0 275,157.5 550,315" fill="var(--ink-graphite)"/>
    </svg>
    <div class="wordmark">VARNHOLT INSIGHT</div>
  </section>

  <section class="card card--back" aria-label="Card back">
    <svg class="facets" viewBox="0 0 550 315" preserveAspectRatio="none" aria-hidden="true">
      <rect width="550" height="315" fill="var(--ink-black)"/>
      <polygon points="0,0 550,0 275,157.5" fill="var(--ink-graphite)"/>
      <polygon points="0,315 550,315 275,157.5" fill="var(--ink-graphite)"/>
    </svg>
    <div class="holder holder__name">JOHN DOE</div>
    <div class="holder holder__title">TITLE</div>
    <div class="holder holder__contact">ADDRESS | ETC</div>
  </section>

</main>
</body>
</html>
```